Box Design for Flooring product

***IMPORTANT: PLEASE READ THE DOCUMENT PROVIDED WITH THIS BRIEF CAREFULLY BEFORE ACCEPTING THIS PROJECT***
Need a creative design for the packaging of a flooring product. The packaging is two boxes: one holding 36 planks of flooring, and the other 7 planks of flooring. There are 4 colours for the flooring planks that need a box designed (for both the 36 plank box and 7 plank box). The boxes measures 92 cm x 16cm x 7cm (36 planks) and 92 cm x 16cm x 1.5cm (7 planks).
More details are provided in the requirements document attached with this brief. Also attaching other supporting documents with this brief mentioned in the document.
Need extra days to review
- Montserrat-Regular

```html
<!DOCTYPE html>
<html lang="en">
<head>
<meta charset="UTF-8">
<title>Stradello Flooring Box</title>
<link href="https://fonts.googleapis.com/css2?family=Montserrat:wght@400;500;600;700&display=swap" rel="stylesheet">
<style>
  :root {
    --brown: #6d6457;
    --brown-dark: #5a5247;
    --white: #ffffff;
    --paper: #f7f6f3;
    --bg: #e4e1dc;
    --ink: #3e3a34;
    --photo-a: #d9d6d2;
    --photo-b: #9c9893;
    --tan: #c9a57a;
  }
  * { margin: 0; padding: 0; box-sizing: border-box; }
  html, body { width: 1200px; height: 869px; overflow: hidden; }
  body { background: var(--bg); font-family: "Montserrat", sans-serif; color: var(--ink); position: relative; }

  .box { position: absolute; left: 40px; width: 1120px; }
  .box--front { top: 40px; }
  .box--back { top: 460px; }

  .lid { height: 64px; background: var(--paper); position: relative; border-bottom: 1px solid #d6d3cd; }
  .lid__inner { position: absolute; inset: 0; transform: rotate(180deg); }
  .lid__features { position: absolute; left: 20px; top: 8px; font-size: 7.5px; line-height: 9px; list-style: disc; padding-left: 10px; color: var(--ink); }
  .lid__brand { position: absolute; left: 380px; top: 12px; display: flex; align-items: center; gap: 8px; }
  .lid__mark { width: 22px; height: 22px; background: var(--brown); }
  .lid__name { font-size: 26px; font-weight: 600; color: var(--brown); letter-spacing: 1px; line-height: 1; }
  .lid__tag { position: absolute; left: 410px; top: 40px; font-size: 8px; letter-spacing: 3px; color: var(--brown); }
  .lid__cert { position: absolute; right: 40px; top: 10px; width: 110px; height: 42px; border: 1px solid var(--ink); background: var(--white); }

  .face { height: 220px; position: relative; overflow: hidden; }
  .face--front { background: var(--white); }
  .face--back { background: var(--brown); height: 240px; color: var(--white); }

  .brand { position: absolute; left: 300px; top: 70px; }
  .brand__name { font-size: 66px; font-weight: 500; color: var(--brown); letter-spacing: 2px; line-height: 1; }
  .brand__tag { font-size: 17px; font-weight: 500; color: var(--brown); letter-spacing: 6.2px; margin-top: 8px; }
  .front-art { position: absolute; inset: 0; }

  .step { position: absolute; font-size: 5.6px; line-height: 6.8px; }
  .step h3 { font-size: 8.5px; font-weight: 500; line-height: 9.5px; margin-bottom: 3px; }
  .step ol { padding-left: 9px; }
  .shot { position: absolute; background: linear-gradient(135deg, var(--photo-a), var(--photo-b)); }
  .shot--floor { background: linear-gradient(135deg, #e0c49e, var(--tan)); }
  .shot--plank { background: linear-gradient(135deg, #b8b6b2, #7f7c78); }
</style>
</head>
<body>

<section class="box box--front">
  <div class="lid">
    <div class="lid__inner">
      <ul class="lid__features">
        <li>Easy to lay</li>
        <li>Water resistant, easy to clean</li>
        <li>Ideal for Bathrooms and Kitchens</li>
        <li>Pack coverage 1m2 (7 planks per pack) - for 5m2 box</li>
        <li>Plank size 914mm x 152mm (36" x 6" approx)</li>
        <li>Suitable for general domestic use</li>
      </ul>
      <div class="lid__brand"><span class="lid__mark"></span><span class="lid__name">STRADELLO</span></div>
      <div class="lid__tag">PREMIUM FLOORS AND TILES</div>
      <div class="lid__cert"></div>
    </div>
  </div>
  <div class="face face--front">
    <svg class="front-art" width="1120" height="220" viewBox="0 0 1120 220">
      <defs>
        <linearGradient id="roomTones" x1="0" y1="0" x2="1" y2="1">
          <stop offset="0" stop-color="#e9e8e6"/>
          <stop offset="0.6" stop-color="#c7c4c1"/>
          <stop offset="1" stop-color="#b3383a"/>
        </linearGradient>
      </defs>
      <polygon points="770,220 880,0 915,0 805,220" fill="#6d6457"/>
      <polygon points="840,220 950,0 1120,0 1120,220" fill="url(#roomTones)" role="img" aria-label="Bedroom scene with grey wood-look flooring planks, bedside table and bed"/>
    </svg>
    <div class="brand">
      <div class="brand__name">STRADELLO</div>
      <div class="brand__tag">PREMIUM FLOORS AND TILES</div>
    </div>
  </div>
</section>

<section class="box box--back">
  <div class="lid">
    <div class="lid__inner">
      <ul class="lid__features">
        <li>Easy to lay</li>
        <li>Water resistant, easy to clean</li>
        <li>Ideal for Bathrooms and Kitchens</li>
        <li>Pack coverage 1m2 (7 planks per pack) - for 5m2 box</li>
        <li>Plank size 914mm x 152mm (36" x 6" approx)</li>
        <li>Suitable for general domestic use</li>
      </ul>
      <div class="lid__brand"><span class="lid__mark"></span><span class="lid__name">STRADELLO</span></div>
      <div class="lid__tag">PREMIUM FLOORS AND TILES</div>
      <div class="lid__cert"></div>
    </div>
  </div>
  <div class="face face--back">
    <div class="step" style="left:10px;top:12px;width:90px;">
      <h3>Step 1:<br>Tools Needed</h3>
      <ol><li>Craft knife</li><li>Tape measure</li><li>Pencil</li><li>Right angle ruler</li><li>Long straight edge</li><li>Vacuum &amp; Brush</li></ol>
    </div>
    <div class="step" style="left:10px;top:92px;width:190px;">
      <h3>Step 2: Acclimatize your floor</h3>
      <p>Leave the planks flat in the room for 24 hours before laying. Keep the room at normal heat. Make sure the subfloor is clean, dry and level. Fill any cracks or holes first.</p>
    </div>
    <div class="shot shot--floor" style="left:105px;top:12px;width:60px;height:55px;" role="img" aria-label="Flooring tools laid out on the floor"></div>

    <div class="step" style="left:172px;top:14px;width:75px;">
      <h3>Step 3:<br>Removing<br>Skirting board</h3>
      <p>If needed, remove skirting boards in the room</p>
    </div>
    <div class="shot" style="left:252px;top:14px;width:60px;height:52px;" role="img" aria-label="Removing a skirting board"></div>
    <div class="shot shot--plank" style="left:205px;top:80px;width:60px;height:40px;" role="img" aria-label="Plank being planned"></div>
    <div class="step" style="left:270px;top:80px;width:60px;">
      <h3>Step 4:<br>Planning your remove</h3>
      <p>Divide the room into sections by drawing 2 lines across the floor. Use these lines as your guide.</p>
    </div>
    <div class="shot shot--floor" style="left:335px;top:80px;width:60px;height:55px;" role="img" aria-label="Right angle ruler on the floor"></div>

    <div class="step" style="left:325px;top:16px;width:125px;">
      <h3>Step 5:<br>Get ready to lay</h3>
      <p>Once the floor is clean, vacuum well. Start laying in the middle of the room and work out one section at a time.</p>
    </div>
    <div class="step" style="left:405px;top:80px;width:135px;">
      <h3>Step 6: Dry lay your planks</h3>
      <p>Start at the centre line and dry lay a row of planks to the wall. Check the gap at the end and adjust the start line so the last plank is not too narrow.</p>
    </div>
    <div class="shot shot--floor" style="left:455px;top:14px;width:65px;height:55px;" role="img" aria-label="Person marking the floor"></div>

    <div class="step" style="left:530px;top:16px;width:90px;">
      <h3>Step 7: Arrows on the backing paper</h3>
      <p>Before laying the planks, ensure the arrows on the backing paper point in the same direction</p>
    </div>
    <div class="shot" style="left:630px;top:14px;width:60px;height:55px;" role="img" aria-label="Arrows on plank backing paper"></div>
    <div class="shot shot--plank" style="left:550px;top:82px;width:65px;height:65px;" role="img" aria-label="Grey wood-look plank sample"></div>
    <div class="step" style="left:622px;top:82px;width:60px;">
      <h3>Step 8:<br>Laying the first plank</h3>
      <p>Peel the backing paper off the first plank and press its edge against the start line.</p>
    </div>
    <div class="shot shot--plank" style="left:690px;top:82px;width:60px;height:50px;" role="img" aria-label="Pressing the first plank down"></div>

    <div class="step" style="left:710px;top:16px;width:160px;">
      <h3>Step 9: Laying the remaining planks</h3>
      <p>Continue positioning the planks until you've covered half the room. Fill in the gaps at the edges last.</p>
    </div>
    <div class="step" style="left:760px;top:82px;width:115px;">
      <h3>Step 10:<br>Cutting the planks</h3>
      <p>To cut planks for the edges, place the plank on the last full plank, mark the line and cut with a craft knife.</p>
    </div>
    <div class="shot shot--plank" style="left:880px;top:20px;width:75px;height:60px;" role="img" aria-label="Laying planks across the room"></div>
    <div class="shot shot--floor" style="left:880px;top:92px;width:75px;height:60px;" role="img" aria-label="Cutting a plank with a craft knife"></div>

    <div class="step" style="left:962px;top:20px;width:80px;">
      <h3>Step 11: Breaking the cut plank</h3>
      <p>Break the plank by bending it at the cut line until it snaps.</p>
    </div>
    <div class="shot" style="left:1050px;top:20px;width:60px;height:55px;" role="img" aria-label="Breaking a cut plank by hand"></div>
    <div class="step" style="left:962px;top:95px;width:85px;">
      <h3>Step 12:<br>Laying the cut planks</h3>
      <p>With the backing paper still on, check the cut plank fits. Then remove the paper and press it into place.</p>
    </div>
    <div class="shot shot--floor" style="left:1050px;top:92px;width:60px;height:55px;" role="img" aria-label="Fitting a cut plank at the wall"></div>
  </div>
</section>

</body>
</html>
```